Orva Business Card

we need a business card for flooring business called Orva Flooring, the design should be black and white. we have 2 locations

Marrowdale Showroom
527 Kellerman Road,
Marrowdale VIC 3187

Ashcombe Showroom
462 Bramwell Hwy,
Ashcombe VIC 3215

email : sales@orvaflooring.com.au
(03) 9471 2830

Please inform we sell , Laminate, Hybrid, Timber, carpet and commercial flooring

```html
<!DOCTYPE html>
<html lang="en">
<head>
<meta charset="utf-8">
<title>Orva Flooring Business Card</title>
<link href="https://fonts.googleapis.com/css2?family=Poppins:wght@300;400;600&display=swap" rel="stylesheet">
<style>
:root{
  --ink:#151515;
  --paper:#ffffff;
  --stage:#2a2a2a;
  --rule:#3a3a3a;
  --back-top:#1d1d1f;
  --back-bottom:#0f0f10;
  --light:#f2f2f2;
}
*{margin:0;padding:0;box-sizing:border-box}
html,body{width:1200px;height:1108px;overflow:hidden}
body{background:var(--stage);font-family:'Poppins',sans-serif;position:relative}
.card{position:absolute;top:204px;width:440px;height:700px;border-radius:26px;overflow:hidden}
.card--front{left:120px;background:var(--paper);color:var(--ink)}
.card--back{left:640px;background:var(--back-bottom)}
.brand{position:absolute;top:64px;left:0;right:0;text-align:center}
.brand__name{font-weight:400;font-size:54px;letter-spacing:3px;line-height:1.05}
.brand__sub{font-weight:400;font-size:32px;letter-spacing:4px;margin-top:2px}
.showrooms{position:absolute;top:196px;left:0;right:0;text-align:center;font-size:21px;line-height:1.3}
.showroom + .showroom{margin-top:8px}
.showroom__title{font-weight:600}
.divider{width:170px;height:3px;border-top:1px solid var(--rule);border-bottom:1px solid var(--rule);margin:20px auto 18px}
.contact{font-size:21px;line-height:1.35}
.band{position:absolute;left:0;right:0;bottom:0;height:168px}
.band svg{position:absolute;inset:0}
.band__text{position:absolute;top:36px;left:0;right:0;text-align:center;color:var(--light)}
.band__title{font-weight:600;font-size:20px;letter-spacing:.5px}
.band__list{font-size:21px;line-height:1.35;margin-top:4px}
.back-field{position:absolute;inset:0;background:linear-gradient(155deg,var(--back-top),var(--back-bottom))}
.back-mark{position:absolute;right:70px;bottom:170px;display:flex;align-items:center;gap:10px;color:var(--light);font-weight:300;font-size:40px;letter-spacing:2px}
.back-mark__dot{width:12px;height:12px;border-radius:50%;background:var(--light)}
</style>
</head>
<body>
<section class="card card--front" aria-label="Card front">
  <div class="brand">
    <div class="brand__name">Orva</div>
    <div class="brand__sub">FLOORING</div>
  </div>
  <div class="showrooms">
    <div class="showroom">
      <div class="showroom__title">Marrowdale Showroom</div>
      <div>527 Kellerman Road,</div>
      <div>Marrowdale VIC 3187</div>
    </div>
    <div class="showroom">
      <div class="showroom__title">Ashcombe Showroom</div>
      <div>462 Bramwell Hwy,</div>
      <div>Ashcombe VIC 3215</div>
    </div>
    <div class="divider"></div>
    <div class="contact">
      <div>(03) 9471 2830</div>
      <div>sales@orvaflooring.com.au</div>
    </div>
  </div>
  <div class="band">
    <svg width="440" height="168" viewBox="0 0 440 168" aria-hidden="true">
      <path d="M0 18 H206 L220 2 L234 18 H440 V168 H0 Z" fill="#151515"/>
      <path d="M0 14 H204 L220 -4 L236 14 H440" fill="none" stroke="#151515" stroke-width="1"/>
    </svg>
    <div class="band__text">
      <div class="band__title">WE SELL</div>
      <div class="band__list">Laminate • Hybrid • Timber<br>Carpet • Commercial Flooring</div>
    </div>
  </div>
</section>
<section class="card card--back" aria-label="Card back">
  <div class="back-field" role="img" aria-label="Dark background with a faint repeating brand pattern"></div>
  <div class="back-mark"><span class="back-mark__dot"></span><span>Orva</span></div>
</section>
</body>
</html>
```